Equipment Finance Specialist I work with companies who need the funds to buy their equipment

I would like a business card that stands out on the shelves. I want to be able to hand it to someone and say WOW. This card should have my logo.
You can put color into it I am very open on design and color

What my company does is we deal with dealerships that sell equipment such as Dump Trucks garbage trucks tractors trailers. Customers get referred to us and depending on their time in business we will ask for the following items

Companies that have been in business for more than two years we have a credit application program up to 250K . With this program we need the following items Credit application filled out(which is what I would like to be able for the customer to click on my website to get.) as well as three current month bank statements.

Deals over 250k we will need the following items

2 years business tax returns
2 years personal tax returns
Profit & Loss statement
Personal Financial Statement

what we do
100% FINANCING
SEASONAL PAYMENTS
LOAN BALLOON PAYMENTS
TRAC LEASING
LOW-INTEREST REFINANCING RATES
DEBT CONSOLIDATION

We specialize in creative financing solutions and offer a variety of reliable, flexible and expandable lending choices.

Target Market(s)

Trucking Companies

Industry/Entity Type

Trucking Company

Contact Information for Business Card

* $250,000 Application only Program
* Loans from $30,000 to 5,000,000
* Competitive Interest Rates

Font styles to use
Serif
Sans Serif

Colors

Designer to choose colors to be used in the design.

Requirements
Must have
• On the back of the card.
• * $250,000 Application only Program
• * Loans from $30,000 to 5,000,000
• My name, email, website. address
• * Competitive Interest Rates
• * 100% Financing
Nice to have
• I want my logo to pop on the card
• My logo is the great one I would like to use
Should not have
• I am up for your creativity as well

```html
<!DOCTYPE html>
<html lang="en">
<head>
<meta charset="utf-8">
<title>Ridgeway Financing Business Card</title>
<link href="https://fonts.googleapis.com/css2?family=Open+Sans:wght@400;600&family=Roboto+Condensed:wght@700&display=swap" rel="stylesheet">
<style>
  :root {
    --backdrop: #2a2a2b;
    --card-dark: #1c1c1d;
    --card-light: #f4f4f3;
    --ink-white: #ffffff;
    --ink-navy: #1b2f6e;
    --ink-red: #c8102e;
    --ink-grey: #4a4a4a;
    --rule-grey: #c9c9c9;
  }
  * { margin: 0; padding: 0; box-sizing: border-box; }
  html, body {
    width: 1200px; height: 900px; overflow: hidden;
    background: var(--backdrop);
  }
  .canvas {
    position: relative; width: 1200px; height: 900px;
    display: flex; flex-direction: column; align-items: center; justify-content: center; gap: 36px;
  }
  .card {
    position: relative; width: 620px; height: 350px;
    box-shadow: 0 10px 28px rgba(0,0,0,.45);
  }
  /* Front */
  .card--front {
    background: var(--card-dark);
    display: flex; flex-direction: column; align-items: center; justify-content: center;
    padding-top: 10px;
  }
  .brand {
    display: flex; align-items: center; gap: 18px; margin-bottom: 38px;
  }
  .brand__dot {
    width: 64px; height: 64px; border-radius: 50%;
    background: var(--ink-white);
  }
  .brand__name {
    font-family: "Roboto Condensed", sans-serif; font-weight: 700;
    color: var(--ink-white); font-size: 40px; line-height: .95;
    letter-spacing: 1px; text-transform: uppercase;
  }
  .offers {
    font-family: "Open Sans", sans-serif; font-size: 14.5px; line-height: 1.35;
    color: var(--ink-white); text-align: center;
  }
  .offers .sep { font-size: 10px; vertical-align: 2px; margin: 0 4px; }
  /* Back */
  .card--back { background: var(--card-light); }
  .identity {
    position: absolute; right: 326px; top: 120px; text-align: right;
    white-space: nowrap;
  }
  .identity__name {
    font-family: "Roboto Condensed", sans-serif; font-weight: 700;
    font-size: 32px; color: var(--ink-navy); line-height: 1; letter-spacing: .3px;
  }
  .identity__title {
    font-family: "Open Sans", sans-serif; font-weight: 600;
    font-size: 14px; color: var(--ink-red); margin-top: 4px; letter-spacing: .4px;
  }
  .divider {
    position: absolute; left: 312px; top: 112px; width: 1px; height: 74px;
    background: var(--rule-grey);
  }
  .contacts {
    position: absolute; left: 332px; top: 118px; list-style: none;
    font-family: "Open Sans", sans-serif; font-size: 14.5px; color: var(--ink-grey);
    white-space: nowrap;
  }
  .contacts li { display: flex; align-items: center; gap: 10px; height: 22px; }
  .icon { width: 14px; height: 14px; fill: var(--ink-navy); flex: none; }
  .address {
    position: absolute; left: 96px; bottom: 70px;
    display: flex; align-items: center; gap: 8px;
    font-family: "Open Sans", sans-serif; font-size: 15px; color: var(--ink-grey);
  }
</style>
</head>
<body>
<main class="canvas">
  <section class="card card--front">
    <div class="brand">
      <span class="brand__dot"></span>
      <span class="brand__name">Ridgeway<br>Financing</span>
    </div>
    <p class="offers">
      $250,000 Application only Program <span class="sep">●</span> Loans from $30,000 to 5,000,000<br>
      Competitive Interest Rates <span class="sep">●</span> 100% Financing
    </p>
  </section>

  <section class="card card--back">
    <div class="identity">
      <h1 class="identity__name">DANIEL BROOKS</h1>
      <p class="identity__title">CEO/FOUNDER</p>
    </div>
    <div class="divider"></div>
    <ul class="contacts">
      <li>
        <svg class="icon" viewBox="0 0 24 24"><path d="M6.6 10.8a15.1 15.1 0 0 0 6.6 6.6l2.2-2.2c.3-.3.7-.4 1-.2 1.1.4 2.3.6 3.6.6.6 0 1 .4 1 1V20c0 .6-.4 1-1 1A17 17 0 0 1 3 4c0-.6.4-1 1-1h3.5c.6 0 1 .4 1 1 0 1.3.2 2.5.6 3.6.1.3 0 .7-.2 1z"/></svg>
        555 214 8830
      </li>
      <li>
        <svg class="icon" viewBox="0 0 24 24"><path d="M2 5h20v2l-10 6L2 7zM2 9l10 6 10-6v10H2z"/></svg>
        daniel@ridgewayfinancing.com
      </li>
      <li>
        <svg class="icon" viewBox="0 0 24 24"><circle cx="12" cy="12" r="10"/><path d="M2 12h20M12 2c3 3 3 17 0 20M12 2c-3 3-3 17 0 20" stroke="#f4f4f3" stroke-width="1.5" fill="none"/></svg>
        www.ridgewayfinancing.com
      </li>
    </ul>
    <p class="address">
      <svg class="icon" viewBox="0 0 24 24"><path d="M12 2a7 7 0 0 0-7 7c0 5 7 13 7 13s7-8 7-13a7 7 0 0 0-7-7zm0 9.5A2.5 2.5 0 1 1 12 6.5a2.5 2.5 0 0 1 0 5z"/></svg>
      1420 Birchwood Drive, Anchorage, Alaska 99501
    </p>
  </section>
</main>
</body>
</html>
```